HOME IMPROVEMENT Business Card

I want a very unique business card. nothing typical and boring. Im open to you ideas. Ive seen cards with gold and silver or color foil and spot UV coatings. Im looking for something that looks cool and grabs attention. I like rounded corners but am open to all suggestions. We are a home improvement company and I will have a presentation folder printed and a catalog printed also and want to keep that same theme. I love the colors in our logo but I am open at looking at a 3rd color that would work with my logo. I hope that helps.
Card should include
Address
Phone
Fax
Email
Website
Target Market(s)
Home owners, people looking to remodel their home
Industry/Entity Type
Home Improvement
Contact Information for Business Card
2873 Maple Crest Avenue Unit 410
Oak Hollow, Il 60284
Phone
Direct Line
Email
Website
Font styles to use
Other font styles liked:
- IM OPEN MINDED
Requirements
Must have
- High end quality look nothing boring I like rounded corners but am open minded
Nice to have
- WOW. I want something nice and impressive.
Should not have
- ??? Not sure

```html
<!DOCTYPE html>
<html lang="en">
<head>
<meta charset="utf-8">
<title>BuildNest Business Card</title>
<link rel="stylesheet" href="https://fonts.googleapis.com/css2?family=Open+Sans:wght@400;600;700;800&display=swap">
<style>
  :root {
    --brand-green: #0a9b3a;
    --brand-navy: #0e1239;
    --paper: #ffffff;
    --backdrop: #d9dadc;
    --ink-light: #ffffff;
  }
  * { margin: 0; padding: 0; box-sizing: border-box; }
  html, body { width: 1200px; height: 977px; overflow: hidden; }
  body {
    background: var(--backdrop);
    font-family: "Open Sans", Arial, sans-serif;
    display: flex;
    flex-direction: column;
    align-items: center;
    justify-content: center;
    gap: 50px;
  }
  .card {
    position: relative;
    width: 740px;
    height: 423px;
    border-radius: 14px;
    overflow: hidden;
    box-shadow: 0 6px 18px rgba(0,0,0,0.18);
  }
  .card-back {
    background: var(--brand-green);
    display: flex;
    align-items: center;
    justify-content: center;
  }
  .wordmark {
    font-weight: 800;
    letter-spacing: -1px;
    line-height: 1;
  }
  .card-back .wordmark { color: var(--ink-light); font-size: 64px; }
  .card-front { background: var(--paper); }
  .card-shapes { position: absolute; inset: 0; }
  .contact {
    position: absolute;
    left: 62px;
    top: 66px;
    color: var(--ink-light);
  }
  .contact-name { font-size: 27px; font-weight: 600; line-height: 1.1; }
  .contact-title { font-size: 15px; font-weight: 700; margin-top: 4px; }
  .contact-address { font-size: 15px; line-height: 1.45; margin-top: 14px; }
  .contact-list { list-style: none; margin-top: 12px; }
  .contact-list li {
    display: flex;
    align-items: center;
    gap: 14px;
    font-size: 16px;
    line-height: 1.65;
  }
  .contact-list svg { width: 16px; height: 16px; flex: none; fill: var(--ink-light); }
  .front-brand {
    position: absolute;
    left: 460px;
    right: 20px;
    top: 150px;
    display: flex;
    align-items: center;
    justify-content: center;
    gap: 10px;
  }
  .brand-square { width: 14px; height: 14px; background: var(--brand-green); }
  .front-brand .wordmark { color: var(--brand-navy); font-size: 50px; }
</style>
</head>
<body>
  <section class="card card-back" aria-label="Card back">
    <span class="wordmark">BuildNest</span>
  </section>

  <section class="card card-front" aria-label="Card front">
    <svg class="card-shapes" viewBox="0 0 740 423" preserveAspectRatio="none" aria-hidden="true">
      <polygon points="0,0 268,0 445,423 0,423" fill="var(--brand-green)"/>
      <polygon points="274,0 304,0 452,423" fill="var(--brand-navy)"/>
    </svg>

    <div class="contact">
      <p class="contact-name">Daniel Reyes</p>
      <p class="contact-title">Manager</p>
      <p class="contact-address">2873 Maple Crest Avenue Unit 410<br>Oak Hollow, Il 60284</p>
      <ul class="contact-list">
        <li><svg viewBox="0 0 16 16"><path d="M3.5 1l2.5 3-1.5 2c1 2 3 4 5 5l2-1.5 3 2.5-1.5 2.5C7 15 1 9 1 2.5z"/></svg>555 014 2380</li>
        <li><svg viewBox="0 0 16 16"><path d="M4 1h8v14H4zM5.5 2.5v9h5v-9zM7.3 12.5h1.4v1.4H7.3z" fill-rule="evenodd"/></svg>555 014 2381</li>
        <li><svg viewBox="0 0 16 16"><path d="M4 2h7v3H4zM1 6h14v7H1zM4 10h8v5H4z"/></svg>555 014 2382</li>
        <li><svg viewBox="0 0 16 16"><path d="M1 3h14v10H1z"/><path d="M1 3l7 6 7-6" fill="none" stroke="#0a9b3a" stroke-width="1.3"/></svg>info@buildnest.com</li>
        <li><svg viewBox="0 0 16 16"><circle cx="8" cy="8" r="7"/><path d="M1 8h14M8 1c3 3 3 11 0 14M8 1c-3 3-3 11 0 14" fill="none" stroke="#0a9b3a" stroke-width="1"/></svg>www.buildnest.com</li>
      </ul>
    </div>

    <div class="front-brand">
      <span class="brand-square" aria-hidden="true"></span>
      <span class="wordmark">BuildNest</span>
    </div>
  </section>
</body>
</html>
```